Sophrologist needs a cool signage at door entrance

I need signage for dr in sophrology based in Belgium (french speaking). The signed should capture the name the "Mireille Vantoorn" - "Naturopathe-Sophrologue-Reiki" and a catchphrase = (Healthy way of life)
« Fais du bien à ton corps, pour que ton âme ait envie d’y rester »
Requirements
Must have
- Hey,
Thats the instagram account for some inspiration www.instagram.com/mireille_serene_wellbeing
Light colors, green, blue
Healthy way of life
Size is 45cm wide on 30 cm high
The signage will be placed in front off woof pannel

```html
<!DOCTYPE html>
<html lang="fr">
<head>
<meta charset="utf-8">
<title>Mireille Vantoorn – Naturopathe, Sophrologue, Reiki</title>
<link rel="stylesheet" href="https://fonts.googleapis.com/css2?family=Poppins:wght@600;700&display=swap">
<style>
  :root {
    --band-light: #dcf0fc;
    --band-tone: #c4e1f4;
    --accent-teal: #47c3dc;
    --navy: #03476f;
    --panel-white: #ffffff;
  }
  html, body {
    margin: 0;
    padding: 0;
    width: 1200px;
    height: 800px;
    overflow: hidden;
    background: var(--panel-white);
  }
  .sign {
    display: block;
    width: 1200px;
    height: 800px;
    font-family: "Poppins", sans-serif;
  }
  .band-fill { fill: url(#bandTone); }
  .rule { fill: var(--accent-teal); }
  .center-panel { fill: var(--panel-white); }
  .name {
    fill: var(--accent-teal);
    font-weight: 700;
    font-size: 158px;
    letter-spacing: 1px;
  }
  .disciplines {
    fill: var(--navy);
    font-weight: 700;
    font-size: 40px;
  }
  .bullet { fill: var(--accent-teal); }
  .tagline {
    fill: var(--navy);
    font-weight: 700;
    font-size: 90px;
    letter-spacing: 1px;
  }
</style>
</head>
<body>
<svg class="sign" viewBox="0 0 1200 800" xmlns="http://www.w3.org/2000/svg">
  <defs>
    <radialGradient id="bandTone" cx="50%" cy="50%" r="70%">
      <stop offset="0%" stop-color="var(--band-tone)"/>
      <stop offset="100%" stop-color="var(--band-light)"/>
    </radialGradient>
  </defs>

  <rect class="band-fill" x="0" y="0" width="1200" height="134" role="img" aria-label="Motif de mandala bleu clair en fond"/>
  <rect class="band-fill" x="0" y="558" width="1200" height="242" role="img" aria-label="Motif de mandala bleu clair en fond"/>

  <rect class="center-panel" x="0" y="142" width="1200" height="408"/>
  <rect class="rule" x="0" y="134" width="1200" height="8"/>
  <rect class="rule" x="0" y="550" width="1200" height="8"/>

  <text class="name" x="600" y="305" text-anchor="middle">MIREILLE</text>
  <text class="name" x="600" y="438" text-anchor="middle">VANTOORN</text>

  <g class="discipline-line">
    <circle class="bullet" cx="153" cy="496" r="8"/>
    <text class="disciplines" x="182" y="510">NATUROPATHE</text>
    <circle class="bullet" cx="495" cy="496" r="8"/>
    <text class="disciplines" x="520" y="510">SOPHROLOGUE</text>
    <circle class="bullet" cx="860" cy="496" r="8"/>
    <text class="disciplines" x="893" y="510">REIKI</text>
  </g>

  <text class="tagline" x="600" y="704" text-anchor="middle">HEALTHY WAY OF LIFE</text>
</svg>
</body>
</html>
```